Our company is Harlow Rivet & Pin Inc. We serve the OEM Market and have customers across the globe. Custom fastening parts made to print as well as standard fasteners, abrasives, adhesives and vendor managed inventory services. We pride ourselves on reliability, partnership and overall lowest cost of business, with an emphasis on quality and attention to detail. Harlow Rivet does not simply provide products, we provide solutions to save our customers time and money in their supply chain as well as on their assembly lines. Our Customers are in Telecom, Metering, Nuclear, Packaging Equipment, Networking Component, Boat Trailer, Portable Military and Camp Shelters, Knife and Locomotive Heater Industries (varied, but all OEM's). 95% of our customers use Lean and Six Sigma in their operations, and we customize our Vendor Managed Inventory Systems to suit each customer's individual supply chain goals. We have a mechanical engineer on staff who oversees our quality and conformance lab to ensure that customer parts are made to their exacting specifications. We incorporate continuous improvement in every process and task in our business. Texas Orange and Black are the main colors we utilize in our marketing. The final design should communicate reliability, innovation, technical superiority, as well as partnership.

Target Market(s)

Original Equipment Manufacturers - Electronic and Industrial

Industry/Entity Type

Business

Requirements
Must have
• Some animation...eye catching, but not distracting. A contact/request for quote page that connects to a company email address. A balance of graphics, photos and written content. Must be able to edit in Expression Web.

You may use the written content and any photos from our current website www.harlowrivet-sample.com
Should not have
• No cartoons, please.

```html
<!DOCTYPE html>
<html lang="en">
<head>
<meta charset="utf-8">
<title>Harlow Rivet & Pin Inc.</title>
<link rel="stylesheet" href="https://fonts.googleapis.com/css2?family=Roboto:wght@300;400;500;700&display=swap">
<style>
:root{
  --orange:#f07640;
  --orange-text:#f26a35;
  --ink:#222222;
  --body:#3a3a3a;
  --muted:#9a9a9a;
  --panel:#f2f2f2;
  --rule:#dddddd;
  --white:#ffffff;
  --black:#111111;
}
*{box-sizing:border-box;margin:0;padding:0}
html,body{width:966px;height:1200px;overflow:hidden}
body{position:relative;font-family:'Roboto',sans-serif;font-weight:300;color:var(--body);background:var(--white)}
.abs{position:absolute}

/* header */
.masthead{left:0;top:0;width:966px;height:543px;background:var(--orange)}
.utility-links{right:97px;top:11px;font-size:11px;color:var(--white);font-weight:300;white-space:nowrap}
.utility-links span{margin:0 5px}
.search-box{left:696px;top:34px;width:174px;height:20px;background:#8f8f8f;border:1px solid #a9a9a9;border-radius:2px;font-size:9.5px;color:#d8d8d8;padding:4px 8px;line-height:11px}
.search-box svg{position:absolute;right:6px;top:3px}
.brand{left:97px;top:55px;width:263px;height:72px;background:var(--black);border:2px solid var(--white);display:flex;align-items:center;padding-left:16px;gap:12px}
.brand-square{width:44px;height:44px;background:var(--orange)}
.brand-name{font-size:22px;font-weight:500;color:var(--white);line-height:1.1}
.main-nav{right:97px;top:83px;font-size:14.5px;font-weight:400;color:var(--black);white-space:nowrap}
.main-nav span{margin:0 8px}
.hero-shadow{left:140px;top:470px;width:690px;height:34px;border-radius:50%;background:radial-gradient(ellipse at center,rgba(90,30,5,.45) 0%,rgba(90,30,5,0) 70%)}
.hero{left:97px;top:161px;width:772px;height:325px;background:linear-gradient(90deg,#b49a78 0%,#7b7f7c 35%,#5c5a4e 50%,#7b7f7c 65%,#b89c80 100%)}
.hero-arrow{top:283px;width:41px;height:41px;background:var(--white);display:flex;align-items:center;justify-content:center}

/* welcome */
.welcome{left:0;top:543px;width:966px;height:260px;background:var(--panel);border-bottom:1px solid #e2e2e2}
.welcome-photo{left:105px;top:580px;width:241px;height:174px;background:linear-gradient(160deg,#5a4632 0%,#2a1f17 55%,#8a5a2c 100%)}
.welcome-title{left:362px;top:581px;font-size:24.5px;font-weight:300;color:var(--orange-text)}
.welcome-text{left:362px;top:625px;width:500px;font-size:11.3px;line-height:19.3px;color:var(--body);text-align:justify}

/* columns */
.columns{left:0;top:804px;width:966px;height:296px;background:var(--panel)}
.col-title{top:822px;font-size:13px;font-weight:500;color:var(--ink)}
.col-rule{top:845px;height:1px;background:var(--rule)}
.service-name{left:140px;font-size:11.3px;color:var(--ink)}
.service-text{left:104px;width:242px;font-size:11px;line-height:19.3px;color:var(--muted);text-align:justify}
.news-thumb{left:374px;width:37px;height:37px;background:var(--orange);border:1.5px solid var(--black)}
.news-title{left:419px;font-size:11.3px;color:var(--ink)}
.news-date{left:419px;font-size:11.3px;color:var(--ink);font-weight:400}
.news-date.accent{color:var(--orange-text)}
.news-date em{font-size:9px;font-style:italic;font-weight:400;color:#555}
.news-text{left:417px;width:166px;font-size:11px;line-height:19.3px;color:var(--muted);text-align:justify}
.gallery-caption{left:620px;top:861px;font-size:11.3px;color:var(--ink)}
.gallery-frame{left:620px;top:879px;width:241px;height:200px;background:var(--white);box-shadow:0 0 3px rgba(0,0,0,.2)}
.gallery-photo{left:625px;top:884px;width:232px;height:191px;background:linear-gradient(180deg,#9c958c 0%,#c9c3ba 45%,#5e2e2c 70%,#3a3433 100%)}
.gallery-arrow{top:968px;width:22px;height:22px;border-radius:50%;background:rgba(255,255,255,.75);display:flex;align-items:center;justify-content:center}

/* footer */
.footer-links{left:105px;top:1134px;font-size:11.3px;color:var(--ink);font-weight:400;white-space:nowrap}
.footer-links span{margin:0 7px}
.copyright{left:104px;top:1162px;font-size:11.3px;color:#555;white-space:nowrap}
.copyright span{margin:0 7px}
.social{top:1142px;width:25px;height:25px;border-radius:50%}
</style>
</head>
<body>

<header class="abs masthead"></header>
<nav class="abs utility-links">Home <span>|</span>Employment<span>|</span>Site Map</nav>
<div class="abs search-box">Search...
  <svg width="12" height="12" viewBox="0 0 12 12"><circle cx="7" cy="5" r="3.3" fill="none" stroke="#eee" stroke-width="1.3"/><line x1="4.6" y1="7.4" x2="1.5" y2="10.5" stroke="#eee" stroke-width="1.6"/></svg>
</div>
<div class="abs brand"><div class="brand-square"></div><div class="brand-name">Harlow Rivet &amp; Pin</div></div>
<nav class="abs main-nav">Home page<span>|</span>About us<span>|</span>Products<span>|</span>How We Help<span>|</span>Contact Us</nav>

<div class="abs hero-shadow"></div>
<div class="abs hero" role="img" aria-label="Warehouse aisle with steel shelving stocked with boxed fasteners"></div>
<div class="abs hero-arrow" style="left:41px"><svg width="12" height="14" viewBox="0 0 12 14"><polyline points="8,2 3,7 8,12" fill="none" stroke="#444" stroke-width="2.4"/></svg></div>
<div class="abs hero-arrow" style="left:877px"><svg width="12" height="14" viewBox="0 0 12 14"><polyline points="4,2 9,7 4,12" fill="none" stroke="#444" stroke-width="2.4"/></svg></div>

<section class="abs welcome"></section>
<div class="abs welcome-photo" role="img" aria-label="Company office interior with reception desk and workstations"></div>
<h1 class="abs welcome-title">Welcome to Harlow Rivet Online.</h1>
<p class="abs welcome-text">Since 1972, Harlow Rivet's mission has been to form strong partnerships with top Inland Northwest companies who share the philosophy of &nbsp;exceptional quality and high integrity. We continue to be successful by focusing on our customers' needs by providing many value-added services as well as treating them fairly, ethically and competitively with every transaction.<br>&nbsp;Our VMI (keepfill) programs are electronically set to your maximum desired quantities...we will not overstock your bins.Streamlined operations mean no waiting in line, getting you back on the job quickly to satisfy YOUR customers.</p>

<section class="abs columns"></section>

<h2 class="abs col-title" style="left:104px">What we do?</h2>
<div class="abs col-rule" style="left:104px;width:242px"></div>
<svg class="abs" style="left:108px;top:852px" width="14" height="32" viewBox="0 0 14 32"><rect x="3" y="1" width="8" height="10" rx="1" fill="#333"/><path d="M1 12h12l-2 9H3z" fill="#333"/><rect x="4" y="22" width="6" height="5" fill="#555"/><rect x="5.5" y="27" width="3" height="3" fill="#333"/></svg>
<div class="abs service-name" style="top:862px">Vendor Managed Inventory</div>
<p class="abs service-text" style="top:891px">Reliable and cost-effective VMI solutions that increase your inventory turns and improve your cash flow...</p>
<div class="abs col-rule" style="left:104px;top:961px;width:222px;background:#e4e4e4"></div>
<svg class="abs" style="left:109px;top:968px" width="22" height="28" viewBox="0 0 22 28"><path d="M6 14 2 26l4-2 2 4 3-10zM16 14l4 12-4-2-2 4-3-10z" fill="#333"/><circle cx="11" cy="10" r="8.5" fill="#333"/><text x="11" y="14" font-size="10" font-family="Roboto,sans-serif" font-weight="700" fill="#fff" text-anchor="middle">1</text></svg>
<div class="abs service-name" style="top:977px">Consistent Quality</div>
<p class="abs service-text" style="top:1007px">Reliable and cost-effective VMI solutions that increase your inventory turns and improve your cash flow...</p>

<h2 class="abs col-title" style="left:361px">Latest News</h2>
<div class="abs col-rule" style="left:361px;width:242px"></div>
<div class="abs news-thumb" style="top:862px"></div>
<div class="abs news-title" style="top:864px">Lorem ipsum dolor sit amet</div>
<div class="abs news-date" style="top:883px">JUNE 2013 <em>Posted By Dana</em></div>
<p class="abs news-text" style="top:901px">Lorem ipsum dolor sit amet, consectetur adipisicing</p>
<div class="abs col-rule" style="left:382px;top:954px;width:201px;background:#e4e4e4"></div>
<div class="abs news-thumb" style="top:978px"></div>
<div class="abs news-title" style="top:980px">Lorem ipsum dolor sit amet</div>
<div class="abs news-date accent" style="top:999px">JUNE 2013 <em>Posted By Dana</em></div>
<p class="abs news-text" style="top:1025px">Lorem ipsum dolor sit amet, consectetur adipisicing elit, sed do eiusmod tempor incididunt</p>

<h2 class="abs col-title" style="left:617px">Harlow Photos</h2>
<div class="abs col-rule" style="left:617px;width:244px"></div>
<div class="abs gallery-caption">Harlow's Office &amp; Conference Room</div>
<div class="abs gallery-frame"></div>
<div class="abs gallery-photo" role="img" aria-label="Conference room with long table and black office chairs"></div>
<div class="abs gallery-arrow" style="left:633px"><svg width="8" height="10" viewBox="0 0 8 10"><polyline points="6,1 2,5 6,9" fill="none" stroke="#555" stroke-width="1.8"/></svg></div>
<div class="abs gallery-arrow" style="left:828px"><svg width="8" height="10" viewBox="0 0 8 10"><polyline points="2,1 6,5 2,9" fill="none" stroke="#555" stroke-width="1.8"/></svg></div>

<footer>
  <nav class="abs footer-links">Home page<span>|</span>About us<span>|</span>Products<span>|</span>How We Help<span>|</span>Contact Us</nav>
  <div class="abs copyright">©2013 Company Name , All Rights Reserved<span>|</span>Privacy Policy<span>|</span> Terms &amp; Conditions</div>
  <div class="abs social" style="left:746px;background:#3b5a9a"></div>
  <div class="abs social" style="left:775px;background:#f28a1e"></div>
  <div class="abs social" style="left:806px;background:#2aa3e0"></div>
  <div class="abs social" style="left:836px;background:#e0262b"></div>
</footer>

</body>
</html>
```